User-interface and web design for new forum-style communication platform

We developed a new forum-style communication platform specially targetting stock investors to share and discuss information on companies listed on the stock exchange.

You have complete freedom for designing the user-interface and web design. Designs should include all features listed below.

Please read the attached document for full specifications. Also attached is a mockup of the layout, but this is only directional. A mockup for the user-profile is also attached, but does not need to be designed.

This project focusses on the homepage and thread view.

The winner(s) will be asked to design the complete project. (create thread box, user profile, registering, settings...)

We are looking for a well thought out, smart design that incorporates the specifications in the attached document. Please do not hesitate to contact us if anything is not clear.

Target Market(s)

Stock investors from 25 to 60 years old (the people that are currently on investor forums)

Industry/Entity Type

Communication

Font styles to use
Sans Serif

Colors

Designer to choose colors to be used in the design.

Requirements
Must have
• Full homepage design & Thread view specified in the attached document.
Nice to have
• Create thread view
- Field for adding tags
- field for subject of the thread
- text box with basic text editing
- method for sharing media
Should not have
• Logo design.

```html
<!DOCTYPE html>
<html lang="en">
<head>
<meta charset="utf-8">
<title>Forum – Public conversations</title>
<link href="https://fonts.googleapis.com/css2?family=Open+Sans:wght@400;600;700&display=swap" rel="stylesheet">
<style>
:root{
  --ink:#333;
  --muted:#666;
  --dark:#3d3935;
  --black:#1b1b1b;
  --blue:#0b95e0;
  --blue-bar:#1fa8ec;
  --orange:#f5a42a;
  --page:#efece6;
  --line:#dedede;
  --panel:#f2f2f2;
  --frame:#d6d4d0;
}
*{box-sizing:border-box;margin:0;padding:0}
html,body{width:1200px;height:1006px;overflow:hidden}
body{position:relative;background:var(--page);font-family:'Open Sans',Arial,sans-serif;color:var(--ink)}
a{color:var(--blue)}
.abs{position:absolute}

/* header */
.topline{position:absolute;left:0;top:0;width:1200px;height:4px;background:var(--dark)}
.header{position:absolute;left:0;top:4px;width:1200px;height:115px;background:linear-gradient(#fdfdfd,#ececec);border-bottom:1px solid #d2d2d2}
.brand{position:absolute;left:110px;top:4px;width:171px;height:89px;background:var(--dark);color:#fff;font-size:19px;display:flex;align-items:center;justify-content:center}
.search{position:absolute;left:323px;top:50px;width:525px;height:43px;background:#fff;border-top:2px solid #ddd;display:flex}
.search .field{flex:1;display:flex;align-items:center;padding-left:10px;color:#aaa;font-size:13px;gap:12px}
.search .actions{width:102px;background:var(--blue-bar);display:flex;align-items:center;justify-content:center;gap:8px;font-size:13px}
.search .actions a{color:#fff}
.search .actions span{width:1px;height:26px;background:rgba(255,255,255,.4)}
.badge{position:absolute;left:894px;top:50px;width:44px;height:44px;border-radius:50%;background:var(--orange);color:#fff;font-size:17px;font-weight:600;display:flex;align-items:center;justify-content:center}
.user-menu{position:absolute;left:949px;top:52px;width:141px;height:41px;background:var(--black);border:1px solid #000;color:#fff;font-size:16px}
.user-menu .avatar{position:absolute;left:6px;top:5px;width:30px;height:30px;background:linear-gradient(#9aa3ab,#4b4f55);border:1px solid #ddd}
.user-menu .name{position:absolute;left:50px;top:9px}
.user-menu .caret{position:absolute;left:100px;top:0;width:40px;height:39px;border-left:1px solid #333;display:flex;align-items:center;justify-content:center}

/* sidebar */
.panel{position:absolute;left:106px;width:245px;border:4px solid #fff;background:var(--panel);border-radius:3px}
.panel-head{height:34px;background:linear-gradient(#fff,#dcdcdc);border-bottom:1px solid #cfcfcf;display:flex;align-items:center;gap:6px;padding-left:10px;font-size:17px}
.panel-list{padding:0 13px 0 12px;list-style:none}
.panel-list li{height:30px;border-bottom:1px solid var(--line);font-size:13px;color:var(--muted);display:flex;align-items:center}
.panel-list li:first-child{height:42px;padding-top:12px}
.panel .more{display:block;padding:10px 0 0 13px;font-size:12px;height:36px}
.users-body{background:var(--orange);height:53px;padding:14px 11px 0}
.users-body .mini{height:25px;background:#fff;border-radius:2px;display:flex;align-items:center;gap:6px;padding-left:9px;font-size:12px;color:#bbb}

/* main */
.crumbs{position:absolute;left:391px;top:158px;width:543px;height:78px;background:#dedbd6;border-radius:3px}
.crumbs .path{position:absolute;left:8px;top:10px;font-size:13px;color:#666;display:flex;align-items:center;gap:6px}
.tabs{position:absolute;left:7px;top:38px;width:347px;height:32px;background:#fff;display:flex;align-items:center;font-size:13px}
.tabs .on{margin-left:5px;height:27px;padding:0 9px;background:#2e2e2e;color:#fff;font-weight:600;display:flex;align-items:center;letter-spacing:.3px}
.tabs .tab{padding:0 14px 0 17px}
.tabs .sep{width:1px;height:24px;background:#bbb}
.create{position:absolute;left:941px;top:200px;width:149px;height:36px;background:var(--orange);border-radius:2px;color:#fff;font-size:13px;font-weight:600;display:flex;align-items:center;gap:7px;padding-left:6px}

.thread{position:absolute;left:393px;width:702px;height:320px}
.thread .label{position:absolute;left:6px;top:0;font-size:13px}
.card{position:absolute;left:0;top:19px;width:702px;height:232px;background:var(--frame);border-radius:3px;box-shadow:0 2px 6px rgba(0,0,0,.15)}
.card .inner{position:absolute;left:6px;top:6px;width:690px;height:220px;background:#fff}
.photo{position:absolute;left:11px;top:11px;width:100px;height:100px;border:1px solid #ccc;background:linear-gradient(135deg,#e8dcc8,#b9c4cc 55%,#2b3a55)}
.subject{position:absolute;left:120px;top:14px;font-size:13px;color:var(--blue)}
.meta{position:absolute;left:120px;top:31px;font-size:13px;color:#555}
.body{position:absolute;left:120px;top:69px;width:560px;font-size:13px;line-height:16px;color:#333}
.foot{position:absolute;left:120px;top:181px;width:555px;height:26px;font-size:12px;color:#777;display:flex;align-items:center}
.foot .read{color:var(--blue);text-decoration:underline;margin-right:20px}
.foot .stat{display:flex;align-items:center;gap:3px;margin-right:20px}
.foot .btns{margin-left:auto;display:flex;gap:3px}
.btn{height:26px;background:var(--blue);color:#fff;font-size:13px;display:flex;align-items:center;justify-content:center;border-radius:2px}
.reply{position:absolute;left:2px;top:260px;width:695px;height:58px}
.reply .me{position:absolute;left:0;top:0;width:59px;height:58px;background:linear-gradient(#b99a7c,#3c3230)}
.reply .input{position:absolute;left:71px;top:0;width:624px;height:58px;background:#fff;color:#bbb;font-size:15px;padding:19px 11px}
</style>
</head>
<body>
<div class="topline"></div>
<header class="header"></header>
<div class="brand">Company Name</div>

<div class="search">
  <div class="field">
    <svg width="22" height="22" viewBox="0 0 22 22"><circle cx="9" cy="9" r="7" fill="none" stroke="#ccc" stroke-width="3"/><line x1="14" y1="14" x2="20" y2="20" stroke="#ccc" stroke-width="3.5" stroke-linecap="round"/></svg>
    <span>#altora&nbsp; #veltrix</span>
  </div>
  <div class="actions"><a>Save</a><span></span><a>Clear</a></div>
</div>
<div class="badge">03</div>
<div class="user-menu">
  <div class="avatar" role="img" aria-label="User profile photo"></div>
  <span class="name">User</span>
  <span class="caret"><svg width="10" height="6" viewBox="0 0 10 6"><path d="M1 1l4 4 4-4" fill="none" stroke="#fff" stroke-width="1.5"/></svg></span>
</div>

<!-- sidebar -->
<div class="panel" style="top:169px;height:96px;border-color:transparent;background:none">
  <div class="panel-head" style="border:1px solid #ccc">
    <svg width="20" height="20" viewBox="0 0 20 20"><circle cx="10" cy="7" r="4" fill="none" stroke="#333" stroke-width="1.6"/><path d="M3 19c1-5 4-7 7-7s6 2 7 7z" fill="none" stroke="#333" stroke-width="1.6"/></svg>Users
  </div>
  <div class="users-body"><div class="mini"><svg width="12" height="12" viewBox="0 0 12 12"><circle cx="5" cy="5" r="4" fill="none" stroke="#bbb" stroke-width="1.4"/><line x1="8" y1="8" x2="11" y2="11" stroke="#bbb" stroke-width="1.4"/></svg>search</div></div>
</div>

<div class="panel" style="top:275px;height:179px">
  <div class="panel-head"><svg width="15" height="15" viewBox="0 0 15 15" fill="#333"><rect x="0" y="1" width="6" height="6"/><rect x="8" y="0" width="6" height="6" transform="rotate(20 11 3)"/><rect x="0" y="8" width="6" height="6"/><rect x="8" y="8" width="6" height="6"/></svg>Saved filters</div>
  <ul class="panel-list"><li>Item One</li><li>Item Two</li><li>Item Three</li></ul>
  <a class="more">show all</a>
</div>

<div class="panel" style="top:470px;height:179px">
  <div class="panel-head"><svg width="18" height="18" viewBox="0 0 18 18"><path d="M1 2h7l9 9-7 7-9-9z" fill="#333"/><circle cx="5" cy="6" r="1.5" fill="#eee"/></svg>Popular tags</div>
  <ul class="panel-list"><li>Item One</li><li>Item Two</li><li>Item Three</li></ul>
  <a class="more">show all</a>
</div>

<div class="panel" style="top:663px;height:179px">
  <div class="panel-head"><svg width="20" height="18" viewBox="0 0 20 18"><path d="M2 17l3-10 5-5 5 3 3 12z" fill="#333"/></svg>Popular contributors</div>
  <ul class="panel-list"><li>Item One</li><li>Item Two</li><li>Item Three</li></ul>
  <a class="more">show all</a>
</div>

<!-- main -->
<div class="crumbs">
  <div class="path">
    <svg width="18" height="17" viewBox="0 0 18 17" fill="#0b95e0"><path d="M9 0l9 8h-3v9h-4v-5H7v5H3V8H0z"/></svg>
    <a style="margin-left:-4px">Home</a><span>&gt;&gt;</span><a>Conversation</a><span>&gt;&gt;</span><a>Public</a><span>&gt;&gt;</span><span>#Altora&nbsp; #veltrix</span>
  </div>
  <div class="tabs"><span class="on">PUBLIC</span><span class="tab">Following</span><span class="sep"></span><span class="tab" style="padding-left:7px">Contacts</span></div>
</div>
<div class="create">
  <svg width="22" height="22" viewBox="0 0 22 22"><circle cx="11" cy="11" r="9" fill="none" stroke="#fff" stroke-width="1.6"/><path d="M6 11h10M11 6v10" stroke="#fff" stroke-width="1.6"/></svg>CREATE THREAD
</div>

<section class="thread" style="top:264px">
  <div class="label">Thread #01</div>
  <article class="card"><div class="inner">
    <div class="photo" role="img" aria-label="Author portrait photo"></div>
    <div class="subject">Lorem ipusm subject</div>
    <div class="meta">posted by Martin Hale on 01/01/2014 - 15:32</div>
    <p class="body">Lorem Ipsum is simply dummy text of the printing and typesetting industry. Lorem Ipsum has been the industry's standard dummy text ever since the 1500s, when an unknown printer took a galley of type and scrambled it to make a type specimen book. It has survived not only five centuries, but also the leap into electronic typesetting, remaining essentially unchanged. It was popularised in the 1960s</p>
    <div class="foot">
      <span class="read">read more</span>
      <span class="stat"><svg width="16" height="11" viewBox="0 0 16 11"><rect x=".5" y=".5" width="15" height="10" fill="none" stroke="#999"/><path d="M3 8l3-4 3 3 2-2 3 3" fill="none" stroke="#999"/></svg>12 replies</span>
      <span class="stat"><svg width="18" height="12" viewBox="0 0 18 12"><path d="M1 6c3-6 13-6 16 0-3 6-13 6-16 0z" fill="none" stroke="#888" stroke-width="1.4"/><circle cx="9" cy="6" r="2.5" fill="#888"/></svg>250 views</span>
      <span class="btns"><span class="btn" style="width:63px">Reply</span><span class="btn" style="width:63px">Share</span><span class="btn" style="width:73px">Favourite</span></span>
    </div>
  </div></article>
  <div class="reply"><div class="me" role="img" aria-label="Current user portrait photo"></div><div class="input">Type your reply here</div></div>
</section>

<section class="thread" style="top:646px">
  <div class="label">Thread #02</div>
  <article class="card"><div class="inner">
    <div class="photo" role="img" aria-label="Author portrait photo"></div>
    <div class="subject">Lorem ipusm subject</div>
    <div class="meta">posted by Martin Hale on 01/01/2014 - 15:32</div>
    <p class="body">Lorem Ipsum is simply dummy text of the printing and typesetting industry. Lorem Ipsum has been the industry's standard dummy text ever since the 1500s, when an unknown printer took a galley of type and scrambled it to make a type specimen book. It has survived not only five centuries, but also the leap into electronic typesetting, remaining essentially unchanged. It was popularised in the 1960s</p>
    <div class="foot">
      <span class="read">read more</span>
      <span class="stat"><svg width="16" height="11" viewBox="0 0 16 11"><rect x=".5" y=".5" width="15" height="10" fill="none" stroke="#999"/><path d="M3 8l3-4 3 3 2-2 3 3" fill="none" stroke="#999"/></svg>12 replies</span>
      <span class="stat"><svg width="18" height="12" viewBox="0 0 18 12"><path d="M1 6c3-6 13-6 16 0-3 6-13 6-16 0z" fill="none" stroke="#888" stroke-width="1.4"/><circle cx="9" cy="6" r="2.5" fill="#888"/></svg>250 views</span>
      <span class="btns"><span class="btn" style="width:63px">Reply</span><span class="btn" style="width:63px">Share</span><span class="btn" style="width:73px">Favourite</span></span>
    </div>
  </div></article>
  <div class="reply"><div class="me" role="img" aria-label="Current user portrait photo"></div><div class="input">Type your reply here</div></div>
</section>
</body>
</html>
```